Educate
Education
Creative Brief
It an educational site, N.G.O
Likes: Green White Green
above header
http://brevardlearning.org/
http://www.koltrex.org/offices/education/about/index.html

```html
<!DOCTYPE html>
<html lang="en">
<head>
<meta charset="utf-8">
<title>Brightpath Learning – Testimonial</title>
<link href="https://fonts.googleapis.com/css2?family=Arimo:wght@400;700&display=swap" rel="stylesheet">
<style>
  :root {
    --green: #1e8a3c;
    --green-dark: #0f6b2a;
    --green-light: #3fae55;
    --text: #333333;
    --muted: #666666;
    --page: #f4f6f4;
    --white: #ffffff;
    --quote: #d9dcd9;
  }
  * { box-sizing: border-box; margin: 0; padding: 0; }
  html, body { width: 1200px; height: 1000px; overflow: hidden; }
  body {
    font-family: "Arimo", Arial, sans-serif;
    background: linear-gradient(#ffffff 0, var(--page) 180px, var(--page) 100%);
    color: var(--text);
    position: relative;
  }
  .brand {
    position: absolute; left: 70px; top: 56px;
    display: flex; align-items: center; gap: 14px;
  }
  .brand-mark { width: 34px; height: 34px; border-radius: 50%; background: var(--green); }
  .brand-name { font-size: 34px; font-weight: 700; color: var(--green); letter-spacing: 1px; }

  .main-nav {
    position: absolute; left: 325px; top: 90px; width: 805px; height: 46px;
    display: flex; gap: 6px;
  }
  .main-nav a {
    flex: auto; display: flex; align-items: center; justify-content: center;
    background: linear-gradient(var(--green-light), var(--green-dark));
    color: var(--white); font-size: 17px; text-decoration: none;
    border-radius: 4px 4px 0 0;
  }
  .main-nav a.active { background: var(--white); color: var(--green); border: 2px solid var(--green); border-bottom: none; height: 58px; }

  .frame {
    position: absolute; left: 73px; top: 148px; width: 1057px; height: 730px;
    background: var(--green); border-radius: 6px;
  }
  .content {
    position: absolute; left: 17px; top: 14px; width: 680px; height: 702px;
    background: var(--white); border-radius: 6px; padding: 24px 28px;
  }
  .content h1 { font-size: 22px; color: var(--green-dark); font-weight: 700; padding-bottom: 12px; border-bottom: 1px solid #dfe5df; }
  .testimonial { position: relative; margin-top: 22px; padding: 0 10px 0 40px; }
  .testimonial::before, .testimonial::after {
    position: absolute; font-size: 70px; color: var(--quote); font-family: Georgia, serif; line-height: 1;
  }
  .testimonial::before { content: "\201C"; left: 2px; top: -8px; }
  .testimonial::after { content: "\201D"; right: 40px; top: 36px; }
  .testimonial p { font-size: 13.5px; line-height: 16px; color: var(--text); }
  .testimonial cite { display: block; text-align: right; font-style: normal; font-size: 13.5px; color: var(--green); margin-top: 10px; }

  .sidebar { position: absolute; left: 717px; top: 20px; width: 323px; }
  .side-head {
    height: 36px; background: linear-gradient(var(--green-light), var(--green-dark));
    color: var(--white); font-size: 16px; display: flex; align-items: center; justify-content: space-between; padding: 0 12px;
    border: 1px solid #6fc27f; border-radius: 3px; margin-bottom: 6px;
  }
  .side-head svg { width: 22px; height: 22px; }
  .news-box { background: var(--white); padding: 8px; margin-bottom: 6px; }
  .news-item { display: flex; gap: 10px; margin-bottom: 8px; }
  .news-thumb { width: 62px; height: 58px; flex: none; background: linear-gradient(#b56a4a, #4a3a2e); border: 2px solid #ddd; }
  .news-thumb.mono { background: linear-gradient(#9a9a9a, #3a3a3a); }
  .news-item p { font-size: 12.5px; line-height: 14px; color: var(--muted); }
  .news-item p b { color: var(--text); font-weight: 400; }
  .see-all { text-align: right; font-size: 13px; color: var(--green); }
  .promo { position: relative; height: 122px; margin-top: 10px; border: 2px solid var(--white); border-radius: 4px; overflow: hidden; }
  .promo-photo { position: absolute; inset: 0; }
  .promo.donate .promo-photo { background: linear-gradient(100deg, #8a6a4a, #c08a5a 60%, #6a4a32); }
  .promo.education .promo-photo { background: linear-gradient(100deg, #9a7c55, #6d8a5a 50%, #b07050); }
  .promo.programs .promo-photo { background: linear-gradient(100deg, #5a4030, #a7a29a 50%, #e2e0da); }
  .promo-label {
    position: absolute; left: 0; bottom: 6px; padding: 5px 10px 5px 12px;
    background: rgba(255,255,255,0.85); font-size: 13px; line-height: 15px; color: var(--text);
  }
  .promo-label strong { display: block; color: var(--green-dark); font-size: 13px; }

  .site-footer {
    position: absolute; left: 73px; top: 893px; width: 1057px;
    display: flex; justify-content: space-between; font-size: 13px; color: var(--text);
  }
  .social { display: flex; gap: 22px; align-items: center; }
  .social span { display: flex; align-items: center; gap: 6px; }
  .dot { width: 14px; height: 14px; border-radius: 50%; background: var(--green); }
  .sq { width: 14px; height: 14px; background: #e58a2a; }
</style>
</head>
<body>
  <header>
    <div class="brand"><span class="brand-mark"></span><span class="brand-name">BRIGHTPATH LEARNING</span></div>
    <nav class="main-nav">
      <a href="#">Home</a><a href="#">About Us</a><a href="#">Service</a><a href="#">News &amp; Events</a>
      <a href="#">Make a Donation</a><a href="#" class="active">Testimonial</a><a href="#">Contact Us</a>
    </nav>
  </header>

  <main class="frame">
    <section class="content">
      <h1>Testimonial</h1>
      <blockquote class="testimonial"><p>Lorem ipsum dolor sit amet, consectetur adipisicing elit, sed do eiusmod tempor incididunt ut labore et dolore magna aliqua. Ut enim ad minim veniam, quis nostrud exercitation ullamco laboris nisi ut aliquip ex ea commodo consequat. Lorem ipsum dolor sit amet, consectetur adipisicing elit, sed do eiusmod tempor incididunt ut labore et dolore magna aliqua</p><cite>( Mr. John Doe - USA )</cite></blockquote>
      <blockquote class="testimonial"><p>Lorem ipsum dolor sit amet, consectetur adipisicing elit, sed do eiusmod tempor incididunt ut labore et dolore magna aliqua. Ut enim ad minim veniam, quis nostrud exercitation ullamco laboris nisi ut aliquip ex ea commodo consequat. Lorem ipsum dolor sit amet, consectetur adipisicing elit, sed do eiusmod tempor incididunt ut labore et dolore magna aliqua</p><cite>( Mr. John Doe - USA )</cite></blockquote>
      <blockquote class="testimonial"><p>Lorem ipsum dolor sit amet, consectetur adipisicing elit, sed do eiusmod tempor incididunt ut labore et dolore magna aliqua. Ut enim ad minim veniam, quis nostrud exercitation ullamco laboris nisi ut aliquip ex ea commodo consequat. Lorem ipsum dolor sit amet, consectetur adipisicing elit, sed do eiusmod tempor incididunt ut labore et dolore magna aliqua</p><cite>( Mr. John Doe - USA )</cite></blockquote>
      <blockquote class="testimonial"><p>Lorem ipsum dolor sit amet, consectetur adipisicing elit, sed do eiusmod tempor incididunt ut labore et dolore magna aliqua. Ut enim ad minim veniam, quis nostrud exercitation ullamco laboris nisi ut aliquip ex ea commodo consequat. Lorem ipsum dolor sit amet, consectetur adipisicing elit, sed do eiusmod tempor incididunt ut labore et dolore magna aliqua</p><cite>( Mr. John Doe - USA )</cite></blockquote>
      <blockquote class="testimonial"><p>Lorem ipsum dolor sit amet, consectetur adipisicing elit, sed do eiusmod tempor incididunt ut labore et dolore magna aliqua. Ut enim ad minim veniam, quis nostrud exercitation ullamco laboris nisi ut aliquip ex ea commodo consequat. Lorem ipsum dolor sit amet, consectetur adipisicing elit, sed do eiusmod tempor incididunt ut labore et dolore magna aliqua</p><cite>( Mr. John Doe - USA )</cite></blockquote>
    </section>

    <aside class="sidebar">
      <div class="side-head">Annauncements <svg viewBox="0 0 22 22"><rect width="22" height="22" rx="3" fill="#fff"/><path d="M6 9l5 5 5-5" stroke="#1e8a3c" stroke-width="3" fill="none"/></svg></div>
      <div class="news-box">
        <div class="news-item"><div class="news-thumb" role="img" aria-label="Photo of a child"></div><p><b>Lorem ipsum dolor sit amet,</b> Consectetur adipisicing elit, sed do eiusmod tempor incididunt</p></div>
        <div class="news-item"><div class="news-thumb mono" role="img" aria-label="Black and white photo of a child"></div><p><b>Lorem ipsum dolor sit amet,</b> Consectetur adipisicing elit, sed do eiusmod tempor incididunt</p></div>
        <div class="see-all">See All »</div>
      </div>
      <div class="side-head">Informations <svg viewBox="0 0 22 22"><rect width="22" height="22" rx="3" fill="#fff"/><path d="M6 13l5-5 5 5" stroke="#1e8a3c" stroke-width="3" fill="none"/></svg></div>
      <div class="side-head">News &amp; Events <svg viewBox="0 0 22 22"><rect width="22" height="22" rx="3" fill="#fff"/><path d="M6 13l5-5 5 5" stroke="#1e8a3c" stroke-width="3" fill="none"/></svg></div>
      <div class="promo donate"><div class="promo-photo" role="img" aria-label="Photo of a woman and child"></div><div class="promo-label"><strong>DONATE NOW</strong>Support Brightpath Learning</div></div>
      <div class="promo education"><div class="promo-photo" role="img" aria-label="Photo of a group of pupils"></div><div class="promo-label"><strong>EDUCATIONS</strong>See Our Educations here</div></div>
      <div class="promo programs"><div class="promo-photo" role="img" aria-label="Photo of a child at a chalkboard"></div><div class="promo-label"><strong>2010 PROGRAMS</strong>See Our Programs of 2010</div></div>
    </aside>
  </main>

  <footer class="site-footer">
    <span>© Copyright 2010 BRIGHTPATH LEARNING . Allright Reserved</span>
    <div class="social"><span><i class="dot"></i>Chatline</span><span><i class="sq"></i>Subscribe</span></div>
  </footer>
</body>
</html>
```